Business card design for IT consulting company

Looking for a simple, modern, clean business card design.
Open to reworking our existing logo.

Attached is our current business cards which we do not like.
Ideally double sided with something simple on the back.
Rectangle / Horizonal only.
No rounded edges on the card.
White as the dominate color is preferred.

Target Market(s)

clients, legal, oil & gas, medical, professionals

Industry/Entity Type

IT, tech, consulting

Contact Information for Business Card

Name, Title, email, phone, cell, website

Font styles to use
Sans Serif

Requirements
Must have
• Clean design
Should not have
• loud colors or unusual fonts, etc

```html
<!DOCTYPE html>
<html lang="en">
<head>
<meta charset="utf-8">
<title>Korvel Solutions – Business Card</title>
<link rel="stylesheet" href="https://fonts.googleapis.com/css2?family=Inter:wght@700&family=Montserrat:wght@300;400;700&display=swap">
<style>
  :root {
    --stage: #ececec;
    --ink-black: #1b1b1c;
    --navy: #27266e;
    --sun: #fdc82f;
    --coral: #ef3f57;
    --white: #ffffff;
    --text-dark: #1d1d2b;
  }
  * { margin: 0; padding: 0; box-sizing: border-box; }
  html, body {
    width: 1200px; height: 1200px; overflow: hidden;
    background: var(--stage);
  }
  .canvas { position: relative; width: 1200px; height: 1200px; }

  .card { position: absolute; left: 162px; width: 875px; height: 523px; overflow: hidden; }

  /* Front */
  .card-front { top: 62px; background: var(--ink-black); }
  .front-brand {
    position: absolute; inset: 0;
    display: flex; align-items: center; justify-content: center; gap: 34px;
  }
  .brand-square { width: 64px; height: 64px; background: var(--sun); }
  .front-brand .brand-name {
    font-family: "Inter", sans-serif; font-weight: 700;
    font-size: 84px; letter-spacing: -1px; color: var(--white);
  }

  /* Back */
  .card-back { top: 617px; background: var(--white); }
  .identity-panel {
    position: absolute; left: 0; top: 0; width: 432px; height: 261px;
    background: var(--navy); color: var(--white);
    font-family: "Montserrat", sans-serif;
  }
  .person-name { position: absolute; left: 102px; top: 124px; font-size: 37px; font-weight: 700; letter-spacing: 0.3px; }
  .person-title { position: absolute; left: 102px; top: 174px; font-size: 24px; font-weight: 300; }

  .contact-panel {
    position: absolute; left: 0; top: 261px; width: 432px; height: 262px;
    background: var(--sun);
  }
  .contact-list { list-style: none; position: absolute; left: 106px; top: 30px; }
  .contact-item {
    display: flex; align-items: center; height: 41px;
    font-family: "Montserrat", sans-serif; font-size: 20px; color: var(--text-dark);
  }
  .contact-icon { width: 24px; height: 24px; margin-right: 24px; flex: none; }

  .back-brand {
    position: absolute; left: 432px; top: 0; width: 443px; height: 523px;
    display: flex; align-items: center; justify-content: center; gap: 18px;
  }
  .back-brand .brand-square { width: 44px; height: 44px; }
  .back-brand .brand-name {
    font-family: "Inter", sans-serif; font-weight: 700;
    font-size: 64px; letter-spacing: -1px; color: var(--navy);
  }
</style>
</head>
<body>
<main class="canvas">
  <section class="card card-front">
    <div class="front-brand">
      <span class="brand-square"></span>
      <span class="brand-name">Korvel Solutions</span>
    </div>
  </section>

  <section class="card card-back">
    <div class="identity-panel">
      <h1 class="person-name">Daniel Moreau</h1>
      <p class="person-title">IT Consultant</p>
    </div>
    <div class="contact-panel">
      <ul class="contact-list">
        <li class="contact-item">
          <svg class="contact-icon" viewBox="0 0 24 24" aria-hidden="true"><rect x="2" y="5" width="20" height="14" fill="#ef3f57"/><path d="M2 5l10 8 10-8" fill="none" stroke="#fdc82f" stroke-width="1.8"/></svg>
          daniel.moreau@korvel.ca
        </li>
        <li class="contact-item">
          <svg class="contact-icon" viewBox="0 0 24 24" aria-hidden="true"><path d="M6.6 2.5l3 3.4-1.8 2.6c1.3 2.7 3.3 4.7 6 6l2.6-1.8 3.4 3-2 3.6C10.5 19.8 4.2 13.5 3 6.2z" fill="#ef3f57"/></svg>
          (888) 555-0148
        </li>
        <li class="contact-item">
          <svg class="contact-icon" viewBox="0 0 24 24" aria-hidden="true"><rect x="6" y="1.5" width="12" height="21" rx="2" fill="none" stroke="#ef3f57" stroke-width="2"/><circle cx="12" cy="18.5" r="1.3" fill="#ef3f57"/></svg>
          (604) 555-0192
        </li>
        <li class="contact-item">
          <svg class="contact-icon" viewBox="0 0 24 24" aria-hidden="true"><g fill="none" stroke="#ef3f57" stroke-width="1.7"><circle cx="12" cy="12" r="9.5"/><ellipse cx="12" cy="12" rx="4.2" ry="9.5"/><path d="M2.5 12h19M4 7h16M4 17h16"/></g></svg>
          www.korvel.ca
        </li>
      </ul>
    </div>
    <div class="back-brand">
      <span class="brand-square"></span>
      <span class="brand-name">Korvel</span>
    </div>
  </section>
</main>
</body>
</html>
```